Kindle: Flu Poster (1 page)

We are looking to create a 11 by 17 inch 1 page poster.
-- Please Include RV7’s logo
-- Use the colors and font and mimic the feel of from Steady Steps, Bright Days Toolkit - Memory Wellness Handouts - Northern Council for Tribal Longevity (rvseven.example)
--> https://rvseven.example/toolkit-memory-wellness-handouts/
Moto needs to be included and it is: Protect Your Community. Protect Your Elders. Stay Vaccinated.
Include funding statement at the bottom of document - small print:
This project is supported by the Bureau for Public Wellness and Outreach of the U.S. Office of Community Care and Welfare (OCCW) as part of a financial assistance award totaling $20,007,444 with 100 percent funded by BPWO/OCCW. The contents are those of the author(s) and do not necessarily represent the official views of, nor an endorsement, by BPWO/OCCW, or the U.S. Government.

```html
<!DOCTYPE html>
<html lang="en">
<head>
<meta charset="utf-8">
<title>Kindle – Fight the Flu Poster</title>
<link href="https://fonts.googleapis.com/css2?family=Source+Sans+3:wght@400;600;700;900&display=swap" rel="stylesheet">
<style>
  :root {
    --paper: #f4e9da;
    --frame: #e4d2bb;
    --red: #b3262c;
    --blue: #2f6c93;
    --ink: #262421;
    --brand: #3a6f95;
    --photo-a: #8e6a55;
    --photo-b: #6b4a5e;
    --photo-c: #c9a98a;
  }
  * { box-sizing: border-box; margin: 0; padding: 0; }
  html, body { width: 849px; height: 1200px; overflow: hidden; background: var(--paper); }
  body { font-family: "Source Sans 3", Arial, sans-serif; color: var(--ink); }
  .poster {
    position: relative; width: 849px; height: 1200px;
    background: var(--paper);
    border: 18px solid var(--frame);
    overflow: hidden;
  }
  .brand { position: absolute; left: 100px; top: 42px; display: flex; align-items: center; gap: 14px; }
  .brand-mark { width: 16px; height: 16px; background: var(--brand); }
  .brand-name { font-weight: 700; color: var(--brand); font-size: 22px; letter-spacing: .5px; text-transform: uppercase; line-height: 1.1; }
  .brand-name small { display: block; font-size: 19px; }

  .photo { position: absolute; z-index: 0; }
  .photo-elder-standing {
    left: 615px; top: 290px; width: 216px; height: 430px;
    background: linear-gradient(180deg, var(--photo-c) 0%, var(--photo-b) 40%, var(--photo-a) 100%);
    border-radius: 36px 0 0 0;
  }
  .photo-elder-seated {
    left: 405px; top: 680px; width: 205px; height: 200px;
    background: linear-gradient(160deg, var(--photo-c) 0%, var(--photo-a) 55%, var(--photo-b) 100%);
    border-radius: 24px;
  }

  .content { position: absolute; left: 30px; top: 160px; width: 580px; z-index: 1; }
  .title { font-weight: 900; color: var(--red); font-size: 50px; letter-spacing: 1px; line-height: 1; text-transform: uppercase; }
  .motto { font-weight: 700; color: var(--red); font-size: 23px; margin-top: 6px; white-space: nowrap; }
  .headline { font-weight: 700; color: var(--blue); font-size: 40px; margin-top: 10px; line-height: 1.1; }
  .section-lead { font-weight: 700; color: var(--red); font-size: 21px; margin-top: 6px; line-height: 1.2; }
  .section-title { font-weight: 700; color: var(--red); font-size: 23px; line-height: 1.15; margin-top: 16px; }
  .bullets { list-style: none; margin-top: 6px; }
  .bullets li { position: relative; padding-left: 24px; font-size: 21px; line-height: 1.22; margin-bottom: 2px; }
  .bullets li::before {
    content: ""; position: absolute; left: 3px; top: 8px; width: 9px; height: 9px;
    background: var(--red); transform: rotate(45deg);
  }
  .symptoms { width: 360px; }

  .footer { position: absolute; left: 30px; right: 30px; bottom: 22px; display: flex; align-items: center; gap: 22px; z-index: 1; }
  .footer .brand-name { font-size: 24px; white-space: nowrap; }
  .funding { font-size: 9.5px; line-height: 1.3; color: var(--ink); }
</style>
</head>
<body>
<main class="poster">
  <header class="brand">
    <span class="brand-mark"></span>
    <span class="brand-name">RV7<small>Northern Council for Tribal Longevity</small></span>
  </header>

  <div class="photo photo-elder-standing" role="img" aria-label="Photograph of a Native elder woman in a purple blouse and silver jewelry, seated outdoors"></div>
  <div class="photo photo-elder-seated" role="img" aria-label="Photograph of an elderly Native woman wearing a headscarf"></div>

  <section class="content">
    <h1 class="title">Kindle</h1>
    <p class="motto">Protect Your Community. Protect Your Elders. Stay Vaccinated.</p>
    <h2 class="headline">Fight the Flu!</h2>
    <p class="section-lead">American Indian and Alaska Native people face higher risks from the flu.</p>
    <ul class="bullets">
      <li>Anyone can catch the flu.</li>
      <li>Native Elders are at a higher risk of death from the flu and pneumonia.</li>
      <li>The flu vaccine is safe.</li>
      <li>You can’t get the flu from the vaccine.</li>
      <li>Get vaccinated for the flu every year to protect yourself and your loved ones from being exposed to the influenza virus.</li>
    </ul>

    <h3 class="section-title">Signs &amp; Symptoms of the Flu (may take 1 to 4 days to appear after exposure to virus, and symptoms may include)</h3>
    <ul class="bullets symptoms">
      <li>Fever or feeling feverish/chills; though not everyone will have a fever</li>
      <li>Cough</li>
      <li>Muscle or body aches</li>
      <li>Fatigue (feeling very tired)</li>
      <li>Sore throat</li>
      <li>Headache</li>
      <li>Vomiting or diarrhea; mostly common in children</li>
    </ul>

    <h3 class="section-title">Help Prevent the Spread of the flu</h3>
    <ul class="bullets">
      <li>Get the flu vaccine every year.</li>
      <li>Cover your mouth when you cough or sneeze.</li>
      <li>Wash your hands.</li>
      <li>Stay home if you are sick.</li>
      <li>See the doctor for treatment that you are prescribed.</li>
    </ul>
  </section>

  <footer class="footer">
    <span class="brand-name">RV7</span>
    <p class="funding">This project is supported by the Bureau for Public Wellness and Outreach of the U.S. Office of Community Care and Welfare (OCCW) as part of a financial assistance award totaling $20,007,444 with 100 percent funded by BPWO/OCCW. The contents are those of the author(s) and do not necessarily represent the official views of, nor an endorsement, by BPWO/OCCW, or the U.S. Government.</p>
  </footer>
</main>
</body>
</html>
```